Company Real Estate Site Needs A Face Lift

I need a new website for the recent company I formed: Voska Real Estate.
You can use my agent website WWW.PALMIROQ.COM to see the style/brand I already have. I will have areas for Searching for homes on IDX, etc.
I really like this site:
http://www.cranfeltmanorhomes.com/
I have attached my logo as well

Industry/Entity Type

Real Estate

Colors
0255a3
ffffff
cee9f5

```html
<!DOCTYPE html>
<html lang="en">
<head>
<meta charset="utf-8">
<title>Voska Real Estate</title>
<link href="https://fonts.googleapis.com/css2?family=Ubuntu:wght@400;500&display=swap" rel="stylesheet">
<style>
:root{
  --brand-blue:#0255a3;
  --sky:#cee9f5;
  --white:#ffffff;
  --name-blue:#a9d8f2;
  --panel-dark:rgba(38,34,30,.72);
  --sidebar-dark:rgba(32,30,28,.82);
  --footer-band:rgba(228,238,245,.86);
  --copyright-band:rgba(236,240,243,.95);
  --footer-text:#333;
  --accent-line:#4fc3e8;
}
*{margin:0;padding:0;box-sizing:border-box}
html,body{width:1200px;height:882px;overflow:hidden}
body{font-family:"Ubuntu",sans-serif;position:relative;background:#6e5a44}
.room-photo{position:absolute;inset:0;
  background:radial-gradient(ellipse at 55% 35%,#8c8b6a 0%,transparent 40%),
  linear-gradient(180deg,#8a7358 0%,#7a6148 45%,#a0896f 70%,#d9d6d0 100%)}
.content-panel{position:absolute;inset:0}
.sidebar{position:absolute;left:84px;top:3px;width:160px;height:556px}
.sidebar-shape{position:absolute;inset:0}
.brand{position:absolute;left:0;top:0;width:160px;height:150px;display:flex;align-items:center;justify-content:center}
.brand-name{color:var(--white);font-size:16px;font-weight:500;text-align:center;line-height:1.3}
.main-nav{position:absolute;left:18px;top:140px;list-style:none}
.main-nav li{position:absolute;white-space:nowrap;color:var(--white);font-size:13px;transform-origin:left center;transform:rotate(24deg)}
.social{position:absolute;left:32px;top:466px}
.social span{position:absolute;width:18px;height:18px;background:#3b3835;transform:rotate(24deg)}
.agent{position:absolute;left:310px;top:168px}
.agent-name{color:var(--name-blue);font-size:32px;font-weight:500;line-height:1}
.agent-phone{color:var(--white);font-size:29px;font-weight:500;margin-top:4px;margin-left:3px}
.agent-email{color:var(--name-blue);font-size:16.5px;margin-top:5px;margin-left:4px}
.intro{position:absolute;left:314px;top:290px;width:780px;color:var(--white);font-size:15.2px;line-height:26.5px;letter-spacing:.05px}
.footer-band{position:absolute;left:0;top:641px;width:1200px;height:197px;background:var(--footer-band);border-bottom:1px solid var(--accent-line)}
.footer-heading{position:absolute;color:var(--brand-blue);font-size:15px;font-weight:500;top:16px}
.link-list{position:absolute;list-style:none;font-size:10.5px;color:var(--footer-text)}
.link-list li{height:21.2px}
.footer-brand{position:absolute;left:470px;top:58px;width:150px;text-align:center;color:var(--brand-blue);font-size:17px;font-weight:500}
.footer-contact-mini{position:absolute;left:487px;top:149px;font-size:10.5px;color:var(--footer-text);line-height:21px}
.contact-lines{position:absolute;left:700px;top:58px;font-size:10.5px;color:var(--footer-text)}
.contact-lines p{height:21px}
.contact-lines .phone-num{color:var(--brand-blue)}
.contact-lines .gap{height:13px}
.badges{position:absolute;left:900px;top:54px}
.copyright{position:absolute;left:0;top:839px;width:1200px;height:43px;background:var(--copyright-band);font-size:10.5px;color:var(--footer-text);padding:13px 0 0 83px}
</style>
</head>
<body>
<div class="room-photo" role="img" aria-label="Bright living room with armchairs, glass coffee table, fern and large window"></div>

<svg class="content-panel" width="1200" height="882" aria-hidden="true">
  <polygon points="283,95 1200,95 1200,390 283,443" fill="var(--panel-dark)"/>
</svg>

<aside class="sidebar">
  <svg class="sidebar-shape" width="160" height="556" aria-hidden="true">
    <polygon points="0,0 160,0 160,556 0,480" fill="var(--sidebar-dark)"/>
    <line x1="5" y1="4" x2="155" y2="4" stroke="var(--accent-line)" stroke-width="1"/>
    <polyline points="4,10 4,110 155,165" fill="none" stroke="var(--accent-line)" stroke-width="1"/>
  </svg>
  <div class="brand"><span class="brand-name">Voska<br>Real Estate</span></div>
  <ul class="main-nav">
    <li style="top:0">Home</li>
    <li style="top:38px">Search Homes</li>
    <li style="top:76px">Buy</li>
    <li style="top:115px">Sell</li>
    <li style="top:153px">Tours</li>
    <li style="top:191px">Testimonials</li>
    <li style="top:229px">Home Blog</li>
    <li style="top:267px">Contact Us</li>
  </ul>
  <div class="social" aria-hidden="true">
    <span style="left:0;top:0"></span>
    <span style="left:24px;top:11px"></span>
    <span style="left:48px;top:22px"></span>
    <span style="left:72px;top:33px"></span>
  </div>
</aside>

<section class="agent">
  <h1 class="agent-name">DARREN VOSKA</h1>
  <p class="agent-phone">555-014-2738</p>
  <p class="agent-email">darren@voskarealty.com</p>
</section>

<p class="intro">Whether you are a first time buyer, or a home buying expert, finding and purchasing your West Virginia dream home can be an over lming process. If you want to avoid the pitfalls and aggravation often accompanied with buying or selling a home, it may be in your best interest to work with a Realtor. If you are considering buying or selling a home and would like to speak to a Charleston area Real Estate professional, call DARREN VOSKA 555-NET-DVSK (014-2738 ) or email darren@voskarealty.com today.</p>

<footer class="footer-band">
  <h2 class="footer-heading" style="left:88px">MLS NAVIGATION &gt;</h2>
  <ul class="link-list" style="left:116px;top:63px">
    <li>Advanced Search</li><li>Map Search</li><li>Address Search</li>
    <li>Our Featured Listings</li><li>Listing Manager Login</li><li>Email Updates Signup</li>
  </ul>
  <ul class="link-list" style="left:292px;top:60px">
    <li>Listing ID Search</li><li>Open Houses</li><li>Sold/Pending Listings</li>
    <li>Home Valuation Request</li><li>IDX/MLS Sitemap</li><li>Search by City</li>
  </ul>
  <div class="footer-brand">Voska<br>Real Estate</div>
  <div class="footer-contact-mini">555.014.2738<br>DARREN@VOSKAREALTY.COM</div>

  <h2 class="footer-heading" style="left:699px">CONTACT INFO &gt;</h2>
  <div class="contact-lines">
    <p>Owen Harlan, Broker</p>
    <p>27 LINDEN RIDGE ROAD SUITE 110</p>
    <p>ASHFORD HOLLOW, WV 25390</p>
    <p class="gap"></p>
    <p>O : <span class="phone-num">555 - 210 - 7653</span></p>
    <p>F : <span class="phone-num">555 - 210 - 4663</span></p>
  </div>
  <svg class="badges" width="220" height="100" aria-hidden="true">
    <rect x="15" y="10" width="200" height="34" rx="4" fill="#ffffff" opacity=".35"/>
    <rect x="121" y="70" width="64" height="30" fill="none" stroke="#555" stroke-width="1.5"/>
    <rect x="190" y="68" width="30" height="30" fill="none" stroke="#555" stroke-width="1.5"/>
  </svg>
</footer>

<div class="copyright">Copyright © 2014 DARREN VOSKA - 555-014-2738 - darren@voskarealty.com</div>
</body>
</html>
```